Brightpath Dental Studio

Please go to www.brightpathdentalstudio.example and obtain the current company logo.
Doctors name are
Marita Velbonne, DDS
Denis Kalb, DMD
Addresses are
318 Larchmont Ave
Halvern, NJ 07412
201-555-0147
And
872 14th St.
East Marlow Bay, NJ 07318
201-555-0182
Theme of the business card should feel modrrn and similar to the website.
Front side should include company logo, doctors name, addresses, phone numbers.
Back of the card should include blank lines for patient's name. Date and time for next scheduled appointment. And notice of 24-hr cancellation courtesy policy.
Dental

```html
<!DOCTYPE html>
<html lang="en">
<head>
<meta charset="utf-8">
<title>Brightpath Dental Studio – Business Card</title>
<link rel="stylesheet" href="https://fonts.googleapis.com/css2?family=Marcellus&family=Montserrat:wght@700&display=swap">
<style>
  :root {
    --magenta: #ec008c;
    --white: #ffffff;
    --ink: #222222;
    --shade: #d3d2d6;
    --backdrop: #ececec;
  }
  * { margin: 0; padding: 0; box-sizing: border-box; }
  html, body { width: 1000px; height: 1200px; overflow: hidden; background: var(--backdrop); }
  .canvas { position: relative; width: 1000px; height: 1200px; }

  .card {
    position: absolute; left: 121px; width: 758px; height: 490px;
    display: flex; overflow: hidden;
    box-shadow: 0 4px 14px rgba(0,0,0,.18);
  }
  .card--front { top: 92px; }
  .card--back { top: 622px; }

  .panel { position: relative; height: 100%; }
  .panel--magenta { background: var(--magenta); }
  .panel--light { background: linear-gradient(to bottom, var(--white) 0%, var(--white) 73%, var(--shade) 100%); }
  .card--front .panel--magenta { width: 376px; }
  .card--front .panel--light { width: 382px; }
  .card--back .panel--light { width: 378px; }
  .card--back .panel--magenta { width: 380px; }

  .doctor { position: absolute; left: 30px; color: var(--white); }
  .doctor--one { top: 76px; }
  .doctor--two { top: 278px; }
  .row { display: flex; align-items: flex-start; gap: 17px; }
  .row + .row { margin-top: 6px; }
  .icon { width: 22px; height: 22px; flex: none; margin-top: 3px; }
  .doctor-name {
    font-family: "Montserrat", sans-serif; font-weight: 700;
    font-size: 20px; line-height: 26px;
  }
  .detail {
    font-family: "Marcellus", serif; font-size: 20px; line-height: 26px;
  }

  .wordmark {
    position: absolute; left: 0; right: 0; top: 178px;
    display: flex; align-items: center; justify-content: center; gap: 12px;
    font-family: "Marcellus", serif; font-size: 32px; line-height: 38px;
    text-align: center;
  }
  .wordmark--dark { color: var(--ink); }
  .wordmark--light { color: var(--white); }
  .wordmark-dot { width: 16px; height: 16px; border-radius: 50%; flex: none; }
  .wordmark--dark .wordmark-dot { background: var(--magenta); }
  .wordmark--light .wordmark-dot { background: var(--white); }

  .field {
    position: absolute; left: 17px;
    font-family: "Marcellus", serif; color: var(--magenta); font-size: 17px;
  }
  .field--patient { top: 100px; }
  .field--appointment { top: 166px; }
  .field-value { font-size: 15px; margin-left: 14px; }
  .field-note { display: block; font-size: 12px; margin-top: 2px; }
  .policy {
    position: absolute; left: 17px; top: 456px;
    font-family: "Marcellus", serif; color: var(--magenta); font-size: 16px;
    display: flex; align-items: center; gap: 6px;
  }
  .policy::before {
    content: ""; width: 9px; height: 9px; border-radius: 50%; background: var(--magenta);
  }
</style>
</head>
<body>
<main class="canvas">

  <section class="card card--front" aria-label="Card front">
    <div class="panel panel--magenta">
      <div class="doctor doctor--one">
        <div class="row">
          <svg class="icon" viewBox="0 0 22 22" aria-hidden="true"><circle cx="11" cy="11" r="10" fill="#fff"/><circle cx="11" cy="8.5" r="3.2" fill="#ec008c"/><path d="M5.5 16.5c1-3 3-4.3 5.5-4.3s4.5 1.3 5.5 4.3z" fill="#ec008c"/></svg>
          <div class="doctor-name">Marita Velbonne<br>DDS</div>
        </div>
        <div class="row">
          <svg class="icon" viewBox="0 0 22 22" aria-hidden="true"><circle cx="11" cy="11" r="10" fill="#fff"/><path d="M11 4.5a4.3 4.3 0 0 0-4.3 4.3c0 3.2 4.3 8 4.3 8s4.3-4.8 4.3-8A4.3 4.3 0 0 0 11 4.5z" fill="#ec008c"/><circle cx="11" cy="8.8" r="1.6" fill="#fff"/></svg>
          <div class="detail">318 Larchmont Ave<br>Halvern, NJ 07412</div>
        </div>
        <div class="row">
          <svg class="icon" viewBox="0 0 22 22" aria-hidden="true"><circle cx="11" cy="11" r="10" fill="#fff"/><path d="M7.2 5.5l2 .1 1 2.6-1.3 1.1a7 7 0 0 0 3.6 3.6l1.1-1.3 2.6 1 .1 2c-.4.8-1.3 1.2-2.2 1.1-4.3-.6-7.4-3.7-8-8-.1-.9.3-1.8 1.1-2.2z" fill="#ec008c"/></svg>
          <div class="detail">201-555-0147</div>
        </div>
      </div>

      <div class="doctor doctor--two">
        <div class="row">
          <svg class="icon" viewBox="0 0 22 22" aria-hidden="true"><circle cx="11" cy="11" r="10" fill="#fff"/><circle cx="11" cy="8.5" r="3.2" fill="#ec008c"/><path d="M5.5 16.5c1-3 3-4.3 5.5-4.3s4.5 1.3 5.5 4.3z" fill="#ec008c"/></svg>
          <div class="doctor-name">Denis Kalb<br>DMD</div>
        </div>
        <div class="row">
          <svg class="icon" viewBox="0 0 22 22" aria-hidden="true"><circle cx="11" cy="11" r="10" fill="#fff"/><path d="M11 4.5a4.3 4.3 0 0 0-4.3 4.3c0 3.2 4.3 8 4.3 8s4.3-4.8 4.3-8A4.3 4.3 0 0 0 11 4.5z" fill="#ec008c"/><circle cx="11" cy="8.8" r="1.6" fill="#fff"/></svg>
          <div class="detail">872 14th St.<br>East Marlow Bay, NJ 07318</div>
        </div>
        <div class="row">
          <svg class="icon" viewBox="0 0 22 22" aria-hidden="true"><circle cx="11" cy="11" r="10" fill="#fff"/><path d="M7.2 5.5l2 .1 1 2.6-1.3 1.1a7 7 0 0 0 3.6 3.6l1.1-1.3 2.6 1 .1 2c-.4.8-1.3 1.2-2.2 1.1-4.3-.6-7.4-3.7-8-8-.1-.9.3-1.8 1.1-2.2z" fill="#ec008c"/></svg>
          <div class="detail">201-555-0182</div>
        </div>
      </div>
    </div>

    <div class="panel panel--light">
      <div class="wordmark wordmark--dark">
        <span class="wordmark-dot"></span>
        <span>Brightpath<br>Dental Studio</span>
      </div>
    </div>
  </section>

  <section class="card card--back" aria-label="Card back">
    <div class="panel panel--light">
      <p class="field field--patient">Patient's Name :<span class="field-value">xxx-xxx-xxx</span></p>
      <p class="field field--appointment">Next Scheduled Appointment :<span class="field-value">xxx-xxx</span><span class="field-note">(Date &amp; Time)</span></p>
      <p class="policy">Notice of 24-hr cancellation courtesy policy.</p>
    </div>
    <div class="panel panel--magenta">
      <div class="wordmark wordmark--light">
        <span class="wordmark-dot"></span>
        <span>Brightpath<br>Dental Studio</span>
      </div>
    </div>
  </section>

</main>
</body>
</html>
```